Investment company needing business card

We are wanting a business card which looks sharp and easy on the eye. We are thinking of having a business card with the logo embossed on it, to really make it stand out. We will only have a small amount of information of the business card, person's name, position, email address and phone number

Contact Information for Business Card

Danica Pruett
Executive Assistant
+64 21 547 3162
danicap@harwellcapital.co.nz

Requirements
Must have
• Embossed logo
Should not have
• Not to be busy

```html
<!DOCTYPE html>
<html lang="en">
<head>
<meta charset="utf-8">
<title>Harwell Capital – Business Card</title>
<link rel="stylesheet" href="https://fonts.googleapis.com/css2?family=Orbitron:wght@700&family=Open+Sans:wght@700&family=Exo+2:wght@400;600&display=swap">
<style>
  :root {
    --bg: #313131;
    --green: #2db574;
    --green-light: #4fd08f;
    --ink: #0a0a0a;
    --mark-grey: #6e6e6e;
  }
  * { margin: 0; padding: 0; box-sizing: border-box; }
  html, body { width: 1200px; height: 777px; overflow: hidden; background: var(--bg); }
  .card { position: relative; width: 1200px; height: 777px; background: var(--bg); }

  .top-rule {
    position: absolute; left: 0; top: 42px; width: 1156px; height: 5px;
    background: linear-gradient(to bottom, var(--green-light), var(--green));
    border-radius: 0 3px 3px 0;
  }

  .contact-panel {
    position: absolute; left: 253px; top: 268px; width: 947px; height: 309px;
    background: var(--green);
    border-radius: 10px 0 0 10px;
    color: var(--ink);
  }
  .person-name {
    position: absolute; left: 0; right: 0; top: 86px; text-align: center;
    font-family: "Orbitron", sans-serif; font-weight: 700; font-size: 58px;
    line-height: 1; letter-spacing: 1px;
  }
  .person-role {
    position: absolute; left: 0; right: 0; top: 141px; text-align: center;
    font-family: "Open Sans", sans-serif; font-weight: 700; font-size: 38px; line-height: 1;
  }
  .contact-row {
    position: absolute; top: 262px; left: 71px;
    display: flex; align-items: center; gap: 49px;
    font-family: "Exo 2", sans-serif; font-weight: 400; font-size: 31px; line-height: 1;
  }
  .contact-item { display: flex; align-items: center; gap: 10px; }
  .contact-item svg { display: block; }

  .brand-square {
    position: absolute; left: 36px; top: 610px; width: 118px; height: 122px;
    background: var(--mark-grey); border-radius: 6px;
  }
  .brand-name {
    position: absolute; left: 192px; top: 646px;
    font-family: "Exo 2", sans-serif; font-weight: 600; color: var(--green);
    font-size: 50px; letter-spacing: 2px; line-height: 1;
  }
</style>
</head>
<body>
<div class="card">
  <div class="top-rule"></div>

  <section class="contact-panel">
    <h1 class="person-name">Danica Pruett</h1>
    <p class="person-role">Executive Assistant</p>
    <div class="contact-row">
      <span class="contact-item">
        <svg width="28" height="22" viewBox="0 0 28 22" aria-hidden="true">
          <path d="M2 8 C2 2 26 2 26 8 L21 10 L19 6 L9 6 L7 10 Z" fill="#0a0a0a"/>
          <path d="M8 9 L20 9 L25 20 L3 20 Z" fill="#0a0a0a"/>
          <circle cx="14" cy="14" r="3" fill="#2db574"/>
        </svg>
        <span class="contact-phone">+64 21 547 3162</span>
      </span>
      <span class="contact-item">
        <svg width="30" height="22" viewBox="0 0 30 22" aria-hidden="true">
          <rect x="1" y="1" width="28" height="20" fill="none" stroke="#0a0a0a" stroke-width="1.6"/>
          <path d="M1 1 L15 12 L29 1 M1 21 L11 9 M29 21 L19 9" fill="none" stroke="#0a0a0a" stroke-width="1.6"/>
        </svg>
        <span class="contact-email">danicap@harwellcapital.co.nz</span>
      </span>
    </div>
  </section>

  <div class="brand-square"></div>
  <div class="brand-name">Harwell Capital</div>
</div>
</body>
</html>
```